Crime/mystery/thriller novel cover design

I am looking to get a cover designed for a novel. It is a crime/mystery/thriller set in Liverpool, England, between the 1970s and current day. I have permission to use some paintings by an artist for the cover, so it just needs put together and jazzed up. I am looking for something which has a fairly classic feel (so not just pulp airport thriller trash) but with some flair nonetheless.
The novel will be paperback, 127mm x 203mm with approx 18mm spine width. Can be gloss or matt cover, would be interesting to discuss.
The title is:
THE CASTLEMERE TIDE
Author name:
ROBERT J. KELVANSKI
Publisher:
VELUMBRA PUBLISHING LTD (or simply VELUMBRA)

I am still working on the back cover blurb but I will upload this when finished.
There are 4 images I could use for the cover though my favourite is the one called Evening, Harwick Docklands.

```html
<!DOCTYPE html>
<html lang="en">
<head>
<meta charset="utf-8">
<title>The Castlemere Tide — Cover</title>
<link href="https://fonts.googleapis.com/css2?family=Cinzel+Decorative:wght@400;700&display=swap" rel="stylesheet">
<style>
  :root {
    --backdrop: #dfe3e3;
    --sky-deep: #16246e;
    --sky-mid: #2448b4;
    --sky-light: #3565d0;
    --dusk-violet: #5f5596;
    --horizon-orange: #e48a4c;
    --skyline-dark: #3a3450;
    --water-top: #2c3868;
    --water-deep: #0f1734;
    --title-ink: #ffffff;
  }
  * { margin: 0; padding: 0; box-sizing: border-box; }
  html, body {
    width: 1200px;
    height: 1139px;
    overflow: hidden;
    background: var(--backdrop);
  }
  .canvas {
    position: relative;
    width: 1200px;
    height: 1139px;
  }
  .cover {
    position: absolute;
    left: 287px;
    top: 69px;
    width: 626px;
    height: 1000px;
    overflow: hidden;
    font-family: "Cinzel Decorative", serif;
    color: var(--title-ink);
  }
  .cover-painting {
    position: absolute;
    inset: 0;
    background: linear-gradient(
      to bottom,
      var(--sky-deep) 0%,
      var(--sky-mid) 22%,
      var(--sky-light) 42%,
      var(--sky-mid) 54%,
      var(--dusk-violet) 60%,
      var(--horizon-orange) 65%,
      var(--horizon-orange) 68%,
      var(--skyline-dark) 71%,
      var(--water-top) 73%,
      var(--water-deep) 100%
    );
  }
  .title {
    position: absolute;
    left: 0;
    right: 0;
    top: 0;
    font-weight: 400;
    line-height: 1;
    text-shadow: 0 2px 6px rgba(10, 20, 60, 0.45);
  }
  .title-line { position: absolute; white-space: nowrap; }
  .title-the { left: 52px; top: 200px; font-size: 50px; }
  .title-main { left: 48px; top: 252px; font-size: 66px; letter-spacing: -1px; }
  .title-tail { right: 50px; top: 346px; font-size: 50px; }
  .author {
    position: absolute;
    left: 0;
    right: 0;
    top: 922px;
    text-align: center;
    font-size: 34px;
    font-weight: 400;
    white-space: nowrap;
    text-shadow: 0 2px 5px rgba(0, 0, 0, 0.4);
  }
</style>
</head>
<body>
  <div class="canvas">
    <div class="cover">
      <div class="cover-painting" role="img" aria-label="Painting: Evening, Harwick Docklands — a blue clouded evening sky over an orange horizon, a lit waterfront skyline and dark reflecting water"></div>
      <h1 class="title">
        <span class="title-line title-the">THE</span>
        <span class="title-line title-main">CASTLEMERE</span>
        <span class="title-line title-tail">TIDE</span>
      </h1>
      <p class="author">ROBERT J. KELVANSKI</p>
    </div>
  </div>
</body>
</html>
```